TallonCryo Website - Biologics storage and handling

I would like a beginning design on a website for TallonCryo:

A Boston-based company dedicated to sourcing, storing, and supplying biologic materials of all kinds to the life sciences and scientific markets. From starting reagents, to basic and intermediate materials, to final synthesized and engineered products, we provide value throughout the biologics supply chain. TallonCryo provides backup, overflow, emergency, and stocking storage solutions to companies on a temporary or permanent basis. Life sciences companies can take advantage of the fact that the company is located in the middle of the Boston/Cambridge biotechnology corridor in order to have quick and efficient access to their cold chain materials. Out of state companies can leverage TallonCryo’s location for efficient distribution of materials to partner and client organizations. We also provide other value added services to organizations that do not have the local manpower, such as sourcing, supply, and distribution of materials.

The design should be mostly a white background with clean, linear, geometric colors added in according to the blue and orange color scheme represented in the corporate logo attached.

The website needs to communicate reliable service and provide the concept of a company dedicated to handling and providing client biological samples in a secure and efficient manner.

Some local competitors are:
1. Orlen BioServices: www.orlenbio-example.com
2. VaultiCore: www.vaulticore-example.com

From a design perspective, I like the Meridel Thera website:

www.merideltheraexample.com

Target Market(s)

Life sciences companies and other organizations

Industry/Entity Type

Biotechnology

Coding

Coded - Design and coding required

Number of Pages Required

5+ page

Font styles to use
Sans Serif

Colors
3176b5
0455a3
f37122

Requirements
Must have
• Tabs for pages:
About - Company information.
Platform - Inventory and sample management cloud platform; temperature profiling, logging, and reporting.
Services - Refrigeration and freezing services for biological samples, logistics services, sourcing services, courier services.
Updates - News, events, blog.
Login portal - Entry point for getting into platform. Maybe some freemium content here.
Nice to have
• Please be creative about website page sections, vibrant colors according to my established color scheme, and clean, linear, geometric shapes. I would like a white background with nice colors, clean lines and borders, and a very contemporary look. I want o
Should not have
• This is not a Business to Consumer business. This is a Business to Business enterprise. There should not be consumer oriented language. It is more about service and relationship management.

```html
<!DOCTYPE html>
<html lang="en">
<head>
<meta charset="utf-8">
<title>TallonCryo — Sourcing, Storing and Supplying Biologic Materials</title>
<link href="https://fonts.googleapis.com/css2?family=Questrial&family=Lato:wght@400;700&display=swap" rel="stylesheet">
<style>
:root{
  --orange:#f37122;
  --orange-soft:#e98d45;
  --blue:#3176b5;
  --blue-deep:#0455a3;
  --ink:#222;
  --text:#555;
  --white:#fff;
  --rule:#d8d8d8;
  --teal-bar:#2b6a83;
}
*{box-sizing:border-box;margin:0;padding:0}
html,body{width:1200px;height:3194px;overflow:hidden;background:var(--white)}
body{font-family:"Lato",sans-serif;color:var(--text);position:relative}
.display{font-family:"Questrial",sans-serif;font-weight:400;text-transform:uppercase}

/* header + hero */
.hero{position:absolute;top:0;left:0;width:1200px;height:600px;
  background:linear-gradient(100deg,#5b8fa8 0%,#8aa6b0 35%,#d39a6c 62%,#e49159 100%)}
.topbar{position:absolute;left:0;top:0;width:1200px;height:98px;border-bottom:1px solid rgba(255,255,255,.45)}
.brand{position:absolute;left:111px;top:40px;display:flex;align-items:center;gap:10px;color:var(--white);font-family:"Questrial",sans-serif;font-size:26px}
.brand-dot{width:18px;height:18px;border-radius:50%;background:var(--orange)}
.phone{position:absolute;left:812px;top:16px;color:var(--white);font-size:18px;display:flex;align-items:center;gap:8px}
.login{position:absolute;left:991px;top:10px;width:97px;height:36px;border-radius:18px;background:var(--orange);color:var(--white);font-size:17px;display:flex;align-items:center;justify-content:center}
.mainnav{position:absolute;right:112px;top:61px;display:flex;gap:40px;font-size:16px;color:var(--white)}
.mainnav .active{color:var(--orange);border-bottom:2px solid var(--orange);padding-bottom:12px}
.hero-title{position:absolute;top:266px;left:0;width:1200px;text-align:center;color:var(--white);font-size:26px;line-height:40px;letter-spacing:.5px}
.btn-ghost{position:absolute;border:2px solid var(--white);border-radius:22px;color:var(--white);font-size:17px;display:flex;align-items:center;justify-content:center}
.hero .btn-ghost{left:520px;top:363px;width:160px;height:44px}
.arrow{position:absolute}
.dots{position:absolute;left:569px;top:549px;display:flex;gap:8px}
.dots span{width:10px;height:10px;border-radius:50%;background:rgba(255,255,255,.45)}
.dots span:first-child{background:var(--white)}

/* section headings */
.sec-bar{position:absolute;left:576px;width:48px;height:3px;background:var(--teal-bar)}
.sec-title{position:absolute;left:0;width:1200px;text-align:center;font-size:35px;color:var(--ink)}
.sec-sub{position:absolute;left:0;width:1200px;text-align:center;font-size:15px;color:var(--ink)}

.welcome-text{position:absolute;left:158px;top:752px;width:884px;text-align:center;font-size:13.5px;line-height:28.3px;color:var(--text)}

/* services */
.services{position:absolute;left:0;top:979px;width:1200px;height:567px;background:var(--orange-soft)}
.services .sec-bar{background:var(--white);top:84px}
.services .sec-title{color:var(--white);top:100px}
.services .sec-sub{color:var(--white);top:150px}
.svc-card{position:absolute;top:195px;width:227px;height:285px}
.svc-photo{position:absolute;inset:0}
.svc-label{position:absolute;left:0;bottom:0;width:100%;height:76px;background:rgba(30,30,30,.72);color:var(--white);font-size:17px;font-weight:700;text-align:center;display:flex;align-items:center;justify-content:center;line-height:25px}
.svc-card.featured .svc-label{background:rgba(70,130,170,.85)}
.svc-card.featured{box-shadow:0 6px 14px rgba(0,0,0,.25)}

/* news */
.news-card{position:absolute;top:1740px;width:312px}
.news-photo{height:208px}
.news-date{margin-top:24px;font-size:11.5px;color:var(--text);display:flex;gap:6px;align-items:center}
.news-title{margin-top:12px;font-size:18px;color:var(--ink)}
.news-body{margin-top:10px;font-size:13px;line-height:25.5px;color:var(--text)}
.news-more{margin-top:4px;text-align:right;color:var(--orange);font-size:15.5px;font-family:"Questrial",sans-serif}

/* about */
.about{position:absolute;left:0;top:2236px;width:1200px;height:470px;background:linear-gradient(110deg,#5a8cab,#4a7a96 60%,#5d8ca6)}
.about-bar{position:absolute;left:111px;top:85px;width:48px;height:3px;background:var(--orange)}
.about h2{position:absolute;left:111px;top:100px;font-size:36px;color:var(--white)}
.about-text{position:absolute;left:111px;top:164px;width:455px;font-size:13.5px;line-height:28.3px;color:var(--white)}
.about .btn-ghost{left:111px;top:349px;width:155px;height:38px;font-size:16px}
.about-frame{position:absolute;left:620px;top:87px;width:477px;height:289px;border:2px solid var(--orange);border-left:none;border-bottom:none}
.about-video{position:absolute;left:611px;top:95px;width:477px;height:290px}
.play{position:absolute;left:820px;top:214px}

/* partners */
.partners{position:absolute;left:0;top:2706px;width:1200px;height:238px;display:flex;align-items:center;justify-content:center;gap:58px}
.partner{display:flex;align-items:center;gap:8px;font-family:"Lato",sans-serif;font-weight:700;font-size:24px;color:#555}
.partner i{width:20px;height:20px;background:#555;display:block}
.partner i.round{border-radius:50%}

/* footer */
.footnav{position:absolute;left:0;top:2994px;width:1200px;display:flex;justify-content:center;gap:24px;font-size:15px;color:var(--ink);font-weight:700}
.footnav .sep{font-weight:400}
.social{position:absolute;left:527px;top:3048px;display:flex;gap:10px}
.social span{width:42px;height:42px;border-radius:50%;border:1.5px solid #333;display:block}
.foot-rule{position:absolute;left:111px;top:3128px;width:978px;height:1px;background:var(--rule)}
.copy{position:absolute;left:0;top:3152px;width:1200px;text-align:center;font-size:12px;color:var(--ink)}
</style>
</head>
<body>

<section class="hero">
  <div role="img" aria-label="Lab scientist in protective suit working at a microscope, tinted blue and orange" style="position:absolute;inset:0;background:radial-gradient(circle at 75% 45%,rgba(255,255,255,.25),transparent 45%)"></div>
  <header class="topbar">
    <div class="brand"><span class="brand-dot"></span>TallonCryo</div>
    <div class="phone">
      <svg width="24" height="24" viewBox="0 0 24 24" fill="none" stroke="#fff" stroke-width="1.4"><circle cx="12" cy="12" r="11"/><path d="M8 7c0 5 4 9 9 9l1-2-3-1-1 1c-2-1-3-2-4-4l1-1-1-3z"/></svg>
      800 555 0142
    </div>
    <div class="login">LOGIN</div>
    <nav class="mainnav"><span class="active">Home</span><span>About</span><span>Platfrom</span><span>Service</span><span>Updates</span><span>Contact</span></nav>
  </header>
  <h1 class="hero-title display">Sourcing, storing, and supplying<br>biologic materials</h1>
  <div class="btn-ghost">GET STARTED</div>
  <svg class="arrow" style="left:72px;top:323px" width="20" height="36" viewBox="0 0 20 36"><path d="M18 2 2 18l16 16" fill="none" stroke="#fff" stroke-width="2"/></svg>
  <svg class="arrow" style="left:1110px;top:323px" width="20" height="36" viewBox="0 0 20 36"><path d="M2 2l16 16L2 34" fill="none" stroke="#fff" stroke-width="2"/></svg>
  <div class="dots"><span></span><span></span><span></span><span></span></div>
</section>

<section class="welcome">
  <div class="sec-bar" style="top:685px"></div>
  <h2 class="sec-title display" style="top:698px">Welcome to TallonCryo</h2>
  <p class="welcome-text">TallonCryo is dedicated to sourcing, storing, and supplying biologic materials of all kinds to the life sciences and scientific markets. From starting reagents, to basic and intermediate materials, to final synthesized and engineered products, we provide value throughout the biologics supply chain. TallonCryo provides backup, overflow, emergency, and stocking storage solutions to companies on a temporary or permanent basis. Life sciences companies can take advantage of the fact that the company is located in the middle of the Boston/Cambridge biotechnology corridor in order to have quick and efficient access to their cold chain materials...</p>
</section>

<section class="services">
  <div class="sec-bar"></div>
  <h2 class="sec-title display">What we do</h2>
  <p class="sec-sub">Lorem ipsum dolor sit amet, consectetur adipiscing elit, sed do</p>
  <svg class="arrow" style="left:76px;top:326px" width="12" height="24" viewBox="0 0 12 24"><path d="M11 1 1 12l10 11" fill="none" stroke="#fff" stroke-width="1.5"/></svg>
  <svg class="arrow" style="left:1108px;top:326px" width="12" height="24" viewBox="0 0 12 24"><path d="M1 1l10 11L1 23" fill="none" stroke="#fff" stroke-width="1.5"/></svg>
  <article class="svc-card" style="left:112px">
    <div class="svc-photo" role="img" aria-label="Warehouse storage aisles with yellow racking" style="background:linear-gradient(90deg,#c9a52a,#e8e2c8 50%,#c9a52a)"></div>
    <div class="svc-label">cGMP BioPharma<br>Storage</div>
  </article>
  <article class="svc-card" style="left:362px">
    <div class="svc-photo" role="img" aria-label="Calibration instrument with test leads" style="background:linear-gradient(160deg,#e4e4e6,#9a9ca3 60%,#3b3d44)"></div>
    <div class="svc-label">Metrology and<br>Calibration</div>
  </article>
  <article class="svc-card featured" style="left:611px">
    <div class="svc-photo" role="img" aria-label="Laboratory microscopes and equipment" style="background:linear-gradient(160deg,#e7edf1,#b9c7d0 60%,#6f8796)"></div>
    <div class="svc-label">Equipment Rentals<br>and Sales</div>
  </article>
  <article class="svc-card" style="left:862px">
    <div class="svc-photo" role="img" aria-label="Lab monitors displaying sample analysis" style="background:linear-gradient(160deg,#cfe2f0,#7fa7c6 55%,#34607f)"></div>
    <div class="svc-label">Validation and<br>Qualification</div>
  </article>
</section>

<section class="news">
  <div class="sec-bar" style="top:1629px"></div>
  <h2 class="sec-title display" style="top:1641px">News &amp; Updates</h2>
  <p class="sec-sub" style="top:1693px">Lorem ipsum dolor sit amet, consectetur adipiscing elit, sed do</p>
  <article class="news-card" style="left:112px">
    <div class="news-photo" role="img" aria-label="Health and virus icons over an orange background" style="background:linear-gradient(135deg,#e3a27c,#c98765 60%,#e8b89a)"></div>
    <div class="news-date"><svg width="11" height="11" viewBox="0 0 11 11"><rect x=".5" y="1.5" width="10" height="9" fill="none" stroke="#555"/><path d="M.5 4h10" stroke="#555"/></svg>JUNE 7.2020</div>
    <h3 class="news-title">Sed ut perspiciatis unde omnis iste</h3>
    <p class="news-body">Lorem ipsum dolor sit amet,ectetur adipiscing elit, sed do eiusm incididunt ut labore et dolore magna aliqua. Ut enim ad minim veniam, quis nostrud exercitat</p>
    <p class="news-more">CONTINUE READING››</p>
  </article>
  <article class="news-card" style="left:443px">
    <div class="news-photo" role="img" aria-label="Stacks of culture dishes and sample tubes" style="background:linear-gradient(180deg,#9a2a2e,#b8474a 55%,#e9e6e0)"></div>
    <div class="news-date"><svg width="11" height="11" viewBox="0 0 11 11"><rect x=".5" y="1.5" width="10" height="9" fill="none" stroke="#555"/><path d="M.5 4h10" stroke="#555"/></svg>JUNE 7.2020</div>
    <h3 class="news-title">Sed ut perspiciatis unde omnis iste</h3>
    <p class="news-body">Lorem ipsum dolor sit amet,ectetur adipiscing elit, sed do eiusm incididunt ut labore et dolore magna aliqua. Ut enim ad minim veniam, quis nostrud exercitat</p>
    <p class="news-more">CONTINUE READING››</p>
  </article>
  <article class="news-card" style="left:775px">
    <div class="news-photo" role="img" aria-label="Warehouse worker moving boxes on a pallet jack" style="background:linear-gradient(160deg,#eef2f2,#c6b08d 55%,#7fb89a)"></div>
    <div class="news-date"><svg width="11" height="11" viewBox="0 0 11 11"><rect x=".5" y="1.5" width="10" height="9" fill="none" stroke="#555"/><path d="M.5 4h10" stroke="#555"/></svg>JUNE 7.2020</div>
    <h3 class="news-title">Sed ut perspiciatis unde omnis iste</h3>
    <p class="news-body">Lorem ipsum dolor sit amet,ectetur adipiscing elit, sed do eiusm incididunt ut labore et dolore magna aliqua. Ut enim ad minim veniam, quis nostrud exercitat</p>
    <p class="news-more">CONTINUE READING››</p>
  </article>
</section>

<section class="about">
  <div class="about-bar"></div>
  <h2 class="display">About us</h2>
  <p class="about-text">Lorem ipsum dolor sit amet, consectetur adipiscing elit, seiusd tempor incididunt ut labore et dolore magna aliqua. psum suspenltrices gravida. Risus commodo viverra maecenas accumsan lacus vel fas. Lorem ipsum dolor sit amet, consectetur adipiscing elit, sed do eimmpor incididunt ut labore et dolore magna aliqua. psum suspendisse ultrices gravida. Risus commodo viverra maecenas accumsan lacus vel facilisis.</p>
  <div class="btn-ghost">LEARN MORE</div>
  <div class="about-frame"></div>
  <div class="about-video" role="img" aria-label="Video still of a technician operating packaging line equipment" style="background:linear-gradient(120deg,#8e9aa3,#c9cdd0 50%,#7c8890)"></div>
  <svg class="play" width="60" height="60" viewBox="0 0 60 60"><circle cx="30" cy="30" r="27" fill="rgba(0,0,0,.15)" stroke="#fff" stroke-width="4"/><path d="M24 18l18 12-18 12z" fill="#fff"/></svg>
</section>

<section class="partners">
  <svg width="12" height="24" viewBox="0 0 12 24"><path d="M11 1 1 12l10 11" fill="none" stroke="#555" stroke-width="1.5"/></svg>
  <div class="partner"><i class="round"></i>Corvale Labs</div>
  <div class="partner"><i class="round"></i>Nextrine Bio</div>
  <div class="partner">Quorvelt</div>
  <div class="partner"><i></i>Ondrivo</div>
  <div class="partner">Altamere Dx</div>
  <svg width="12" height="24" viewBox="0 0 12 24"><path d="M1 1l10 11L1 23" fill="none" stroke="#555" stroke-width="1.5"/></svg>
</section>

<footer>
  <nav class="footnav"><span>Home</span><span class="sep">|</span><span>About</span><span class="sep">|</span><span>Platfrom</span><span class="sep">|</span><span>Service</span><span class="sep">|</span><span>Updates</span><span class="sep">|</span><span>Contact</span></nav>
  <div class="social"><span aria-label="Social link"></span><span aria-label="Social link"></span><span aria-label="Social link"></span></div>
  <div class="foot-rule"></div>
  <p class="copy">© Copyright 2020. All Rights Reserved. Terms and Conditions | Privacy Policy</p>
</footer>

</body>
</html>
```